Digital Album Cover - Frosted Lanterns (Night Falls Still)

HiI need a digital album cover for a piano instrumental cover single

Artist: Corey Dalton
Title: Frosted Lanterns (Night Falls Still)

The song was originally by Derek Holloway

Please use my logo

You can listen to the track herehttps://soundcloud.com/coreydaltonkeys/frosted-lanterns-night-falls-still-piano-instrumental-cover

Requirements
Must have
• My logo design Corey Dalton

```html
<!DOCTYPE html>
<html lang="en">
<head>
<meta charset="utf-8">
<title>Corey Dalton – Frosted Lanterns (Night Falls Still)</title>
<link rel="stylesheet" href="https://fonts.googleapis.com/css2?family=Kanit:wght@600&family=Montserrat:wght@700&family=Roboto:wght@400;500&display=swap">
<style>
  :root {
    --bg: #111112;
    --ink: #ffffff;
    --tagline: #e2e2e2;
    --petal-core: #cdb58c;
    --petal-warm: #e9e1cc;
    --petal-light: #e4e6ee;
    --petal-mid: #aeb3c4;
    --petal-shade: #4a4f63;
  }
  html, body {
    margin: 0;
    padding: 0;
    width: 1200px;
    height: 1200px;
    overflow: hidden;
    background: var(--bg);
  }
  .cover {
    position: relative;
    width: 1200px;
    height: 1200px;
    background: var(--bg);
    color: var(--ink);
    overflow: hidden;
  }
  .brand-mark {
    position: absolute;
    left: 163px;
    top: 47px;
    width: 204px;
    height: 204px;
    border-radius: 50%;
    background: var(--ink);
  }
  .brand-name {
    position: absolute;
    left: 394px;
    top: 108px;
    margin: 0;
    font-family: "Roboto", Arial, sans-serif;
    font-weight: 500;
    font-size: 76px;
    line-height: 1;
    letter-spacing: 2.5px;
    text-transform: uppercase;
    white-space: nowrap;
  }
  .brand-tagline {
    position: absolute;
    left: 465px;
    top: 202px;
    margin: 0;
    font-family: "Roboto", Arial, sans-serif;
    font-weight: 400;
    font-size: 39px;
    line-height: 1;
    white-space: nowrap;
    color: var(--tagline);
  }
  .rose-photo {
    position: absolute;
    left: 140px;
    top: 230px;
    width: 900px;
    height: 810px;
    background:
      radial-gradient(ellipse 40% 42% at 50% 50%,
        var(--petal-core) 0%,
        var(--petal-warm) 30%,
        var(--petal-light) 55%,
        rgba(228,230,238,0) 100%),
      radial-gradient(ellipse 50% 50% at 50% 50%,
        var(--petal-light) 0%,
        var(--petal-mid) 55%,
        var(--petal-shade) 80%,
        rgba(17,17,18,0) 100%);
  }
  .title {
    position: absolute;
    left: 0;
    width: 1200px;
    top: 976px;
    margin: 0;
    text-align: center;
    font-family: "Kanit", "Trebuchet MS", sans-serif;
    font-weight: 600;
    font-size: 88px;
    line-height: 1;
    text-transform: uppercase;
  }
  .subtitle {
    position: absolute;
    left: 0;
    width: 1200px;
    top: 1080px;
    margin: 0;
    text-align: center;
    font-family: "Montserrat", Arial, sans-serif;
    font-weight: 700;
    font-size: 29px;
    line-height: 1;
    letter-spacing: 3px;
    text-transform: uppercase;
  }
</style>
</head>
<body>
  <main class="cover">
    <div class="rose-photo" role="img" aria-label="Close-up photograph of a single white rose in full bloom, cream at its heart and cool blue-grey at the petal edges, against a black background"></div>

    <div class="brand-mark" aria-hidden="true"></div>
    <p class="brand-name">Corey Dalton</p>
    <p class="brand-tagline">Wedding &amp; Event Pianist</p>

    <h1 class="title">Frosted Lanterns</h1>
    <p class="subtitle">(Night Falls Still)</p>
  </main>
</body>
</html>
```